Meridale Holding Partners Corporate Showcase

Provide an attractive Corporate Website for a boutique Investment Company to showcase our activities and corporate interests.

Our Company works across a number of Sectors including

Real Estate
E-Commerce
Healthcare
Beauty & Personal Care
Technology
Resources

Lets keep the personality

Modern
Global
Sophisticated
Calm
Interesting

Lets keep the pages with MINIMAL Words
Lets use Photos/ Imagery to tell the story

We'll need a Banner Menu -
About Us
Expertise
Global Outlook
Sectors
Management
Media
Contact Us

Many thanks
Best wishes
Derek.

Target Market(s)

Investors
Clients

Coding

Coded - Design and coding required

Number of Pages Required

5+ page

Font styles to use
Sans Serif

Colors
886aae
3176b5
00a990
f68e4d
f04a50
e667a6

Requirements
Must have
• WordPress Coding

Checkout this Website for look and feel - its cool:
www.kvr.com

Meridale Holding Stewardship
(Meridale Holding Partners LLP)
London
E4 2RL
United Kingdom

www.MeridaleHoldingStewardship.com
Nice to have
• Sophisticated colour palette - black/ brown/ blue/ purple/

```html
<!DOCTYPE html>
<html lang="en">
<head>
<meta charset="utf-8">
<title>Meridale Holding Partners</title>
<link rel="stylesheet" href="https://fonts.googleapis.com/css2?family=Bodoni+Moda:wght@400;500;600&family=Jost:wght@300;400;500;600&family=Oswald:wght@400&display=swap">
<style>
:root{
  --ink:#141214;
  --panel:#242022;
  --panel-soft:#2b2728;
  --footer:#1b191a;
  --accent:#ef8a3c;
  --white:#ffffff;
  --muted:#bdb7b3;
  --line:#3a3536;
  --serif:'Bodoni Moda', 'Times New Roman', serif;
  --sans:'Jost', Arial, sans-serif;
}
*{margin:0;padding:0;box-sizing:border-box}
html,body{width:1200px;height:2949px;overflow:hidden;background:var(--ink);font-family:var(--sans);color:var(--white)}
.page{position:relative;width:1200px;height:2949px}
.abs{position:absolute}

/* header */
.site-header{position:absolute;left:0;top:0;width:1200px;height:96px;border-bottom:1px solid rgba(255,255,255,.18);z-index:3}
.brand{position:absolute;left:88px;top:24px;font-family:var(--serif);font-weight:400;font-size:44px;letter-spacing:2px;color:var(--accent);line-height:1}
.nav{position:absolute;top:42px;left:317px;display:flex;gap:0;font-size:11px;letter-spacing:1.2px;font-weight:500;text-transform:uppercase}
.nav a{color:var(--white);text-decoration:none;position:absolute;white-space:nowrap}
.nav a.active{color:var(--accent)}
.btn-contact{position:absolute;left:984px;top:33px;width:128px;height:31px;background:var(--accent);color:var(--ink);font-size:11px;font-weight:500;letter-spacing:1.2px;display:flex;align-items:center;justify-content:center;text-transform:uppercase}

/* hero */
.hero{position:absolute;left:0;top:0;width:1200px;height:639px;background:var(--panel)}
.hero-photo{position:absolute;left:464px;top:0;width:736px;height:639px;background:linear-gradient(160deg,#3d4f6a 0%,#2a3447 40%,#1e2330 75%,#2a2a33 100%)}
.hero-photo::after{content:"";position:absolute;inset:0;background:linear-gradient(90deg,rgba(36,32,34,.55),rgba(36,32,34,0) 45%)}
.hero-title{position:absolute;left:210px;top:264px;font-family:var(--serif);font-size:50px;line-height:58px;font-weight:400;letter-spacing:1px;z-index:2}
.hero-title strong{font-weight:600}
.counter{position:absolute;left:50px;top:352px;font-family:'Oswald',sans-serif;font-size:24px}
.counter small{font-family:var(--sans);font-size:11px;color:var(--muted)}
.text-link{position:absolute;font-size:11px;font-weight:500;letter-spacing:1.2px;color:var(--accent);text-transform:uppercase;padding-left:20px;height:32px;display:flex;align-items:center;border-left:2px solid var(--accent)}

/* services */
.services{position:absolute;left:0;top:639px;width:1200px;height:978px;background:var(--ink)}
.section-title{font-family:var(--serif);font-weight:400;color:var(--white);letter-spacing:1px}
.photo{position:absolute}
.card{position:absolute;width:256px;background:var(--panel);padding:38px 40px}
.card h3{font-family:var(--sans);font-weight:400;font-size:16px;color:var(--accent);text-transform:uppercase;letter-spacing:.3px}
.card p{margin-top:18px;font-size:12px;line-height:19px;color:var(--white);font-weight:400}
.btn-outline{display:inline-flex;align-items:center;justify-content:center;border:2px solid var(--accent);color:var(--accent);font-size:11px;font-weight:500;letter-spacing:1.2px;height:32px;padding:0 20px;text-transform:uppercase}
.card .btn-outline{margin-top:40px}
.card .text-link{position:relative;margin-top:32px}

/* experience */
.experience{position:absolute;left:0;top:1617px;width:1200px;height:456px;background:linear-gradient(120deg,#2e2a2b 0%,#262223 50%,#302c2d 100%)}
.big-number{position:absolute;left:82px;top:1640px;font-family:'Oswald',sans-serif;font-size:390px;line-height:1;color:#6d6a6a;letter-spacing:-8px}
.exp-title{position:absolute;left:210px;top:1794px;font-family:var(--serif);font-size:40px;line-height:46px;font-weight:400;letter-spacing:-.5px;transform:scaleX(.86);transform-origin:left}
.quote{position:absolute;left:616px;top:1716px;width:496px;font-size:17px;line-height:24px;text-transform:uppercase;font-weight:400;letter-spacing:.2px}
.quote em{font-style:normal;color:var(--accent)}
.exp-body{position:absolute;left:616px;top:1808px;width:496px;font-size:12px;line-height:19.3px;text-align:justify;color:#e8e3df}

/* blog */
.blog{position:absolute;left:0;top:2073px;width:1200px;height:595px;background:var(--ink)}
.blog-title{position:absolute;left:0;width:1200px;top:2140px;text-align:center;font-family:var(--serif);font-size:46px;font-weight:400;letter-spacing:1px}
.blog-title strong{font-weight:600}
.post-photo{position:absolute;top:2227px;width:320px;height:200px}
.post-card{position:absolute;top:2387px;width:256px;height:201px;background:var(--panel);padding:28px 40px}
.post-card h4{font-size:16px;line-height:24px;font-weight:400;text-transform:uppercase;letter-spacing:.2px}
.post-card .text-link,.post-card .btn-outline{position:absolute;left:40px;top:132px}

/* footer */
.site-footer{position:absolute;left:0;top:2668px;width:1200px;height:281px;background:var(--footer)}
.footer-brand{position:absolute;left:86px;top:2736px;font-family:var(--serif);font-size:74px;line-height:1;color:var(--accent);letter-spacing:3px}
.footer-head{position:absolute;top:2744px;font-size:13px;font-weight:500;letter-spacing:.4px;text-transform:uppercase}
.footer-call{position:absolute;left:352px;top:2778px;font-size:19px}
.footer-call span{color:var(--accent)}
.footer-small{position:absolute;font-size:12px;color:var(--muted)}
.footer-addr{position:absolute;left:616px;top:2778px;font-size:19px;color:#a9a4a0}
.footer-rule{position:absolute;left:88px;top:2868px;width:1024px;height:1px;background:var(--line)}
.copyright{position:absolute;left:88px;top:2900px;font-size:12px;color:#c9c3bf}
.copyright span{color:var(--accent)}
.social{position:absolute;top:2892px;width:32px;height:32px;border-radius:50%;background:#3a3637}
</style>
</head>
<body>
<div class="page">

  <section class="hero">
    <div class="hero-photo" role="img" aria-label="Upward view of glass skyscrapers against a blue cloudy sky"></div>
    <svg class="abs" style="left:0;top:210px" width="160" height="320" viewBox="0 0 160 320" aria-hidden="true">
      <path d="M0 8 A152 152 0 0 1 0 312" transform="translate(0,0)" fill="none" stroke="#5a5354" stroke-width="1" stroke-dasharray="3 4"/>
      <path d="M71 114 l5 -5 l5 5" fill="none" stroke="#8a8384" stroke-width="1.2"/>
      <path d="M71 200 l5 5 l5 -5" fill="none" stroke="#8a8384" stroke-width="1.2"/>
    </svg>
    <div class="counter">01 <small>/ 04</small></div>
    <h1 class="hero-title">Big thinking for today's<br><strong>biggest business challenges</strong></h1>
    <div class="text-link" style="left:210px;top:430px">Watch video</div>
  </section>

  <header class="site-header">
    <div class="brand">MHP</div>
    <nav class="nav">
      <a class="active" style="left:0">Home</a>
      <a style="left:62px">About us</a>
      <a style="left:157px">Expertise</a>
      <a style="left:255px">Global outlook</a>
      <a style="left:399px">Sectors</a>
      <a style="left:481px">Management</a>
      <a style="left:589px">Media</a>
    </nav>
    <div class="btn-contact">Contact us</div>
  </header>

  <section class="services">
    <h2 class="section-title abs" style="left:210px;top:131px;font-size:34px;line-height:47px">We are a boutique<br>investment company</h2>
  </section>
  <div class="photo" style="left:281px;top:905px;width:335px;height:359px;background:linear-gradient(135deg,#6d7f93,#b9c2c9 45%,#a0582c 80%,#c27a3f)" role="img" aria-label="Hands signing documents over a tablet at a desk"></div>
  <div class="photo" style="left:831px;top:776px;width:161px;height:192px;background:linear-gradient(160deg,#dfe6ec,#9aa8b6 50%,#1f2633)" role="img" aria-label="Smiling businessman in a dark suit at a meeting"></div>
  <div class="photo" style="left:616px;top:968px;width:376px;height:169px;background:linear-gradient(120deg,#c9c4bd,#e9ecef 45%,#7d8fa5 80%,#cfd5dc)" role="img" aria-label="Team around a table with laptops and charts"></div>
  <div class="photo" style="left:616px;top:1137px;width:376px;height:360px;background:linear-gradient(135deg,#4d5561,#8a8f86 40%,#d9dee4 70%,#6b8fb3)" role="img" aria-label="Businessmen reviewing financial charts on a tablet"></div>

  <div class="card" style="left:576px;top:736px;height:232px">
    <h3>Expertise</h3>
    <p>Lorem Ipsum is simply dummy text of the printing and typ setting industry ...</p>
    <span class="btn-outline">Read more</span>
  </div>
  <div class="card" style="left:248px;top:1073px;height:231px">
    <h3>Global outlook</h3>
    <p>Lorem Ipsum is simply dummy text of the printing and typ setting industry ...</p>
    <div class="text-link">Read more</div>
  </div>
  <div class="card" style="left:576px;top:1304px;height:233px">
    <h3>Management</h3>
    <p>Lorem Ipsum is simply dummy text of the printing and typ setting industry ...</p>
    <div class="text-link">Read more</div>
  </div>

  <section class="experience" role="img" aria-label="Faint background of city towers"></section>
  <div class="big-number">13</div>
  <h2 class="exp-title">Years of successful<br>Experience</h2>
  <p class="quote">"Sed ut perspiciatis <em>unde omnis iste natus</em> error sit remav voluptatem accusantium doloremque <em>laudan-tium, totam</em> rem aperiam</p>
  <p class="exp-body">Nemo enim ipsam voluptatem quia voluptas sit aspernatur aut odit aut fugit, sed quia consequuntur magni dolores eos qui ratione voluptatem sequi nesciunt. Neque porro quisquam est, qui dolorem ipsum quia dolor sit amet, consectetur, adipisci velit, sed quia non numquam eius modi tempora incidunt ut labore et dolore magnam aliquam quaerat voluptatem. Ut enim ad minima ...</p>
  <div class="text-link" style="left:616px;top:1938px">About us</div>

  <section class="blog"></section>
  <h2 class="blog-title">Latest <strong>blog post</strong></h2>

  <div class="post-photo" style="left:88px;background:linear-gradient(135deg,#6a5a4a,#b7ab9a 45%,#3b3f48)" role="img" aria-label="Hands working on a tablet over business reports"></div>
  <div class="post-photo" style="left:441px;background:linear-gradient(135deg,#d9dee3,#8c96a1 50%,#2b303a)" role="img" aria-label="Colleagues talking in a bright office"></div>
  <div class="post-photo" style="left:792px;background:linear-gradient(135deg,#4a515c,#9aa09b 45%,#d5dce4 70%,#6d93b8)" role="img" aria-label="Business charts on a tablet in hand"></div>

  <article class="post-card" style="left:120px">
    <h4>There are many<br>variations of pas-<br>sages of ...</h4>
    <div class="text-link">Read more</div>
  </article>
  <article class="post-card" style="left:472px">
    <h4>There are many<br>variations of pas-<br>sages of ...</h4>
    <span class="btn-outline">Read more</span>
  </article>
  <article class="post-card" style="left:824px">
    <h4>There are many<br>variations of pas-<br>sages of ...</h4>
    <div class="text-link">Read more</div>
  </article>

  <footer class="site-footer"></footer>
  <div class="footer-brand">MHP</div>
  <div class="footer-head" style="left:352px">Contact us</div>
  <div class="footer-call">Call: <span>020-555-0143</span></div>
  <div class="footer-small" style="left:352px;top:2809px"><b style="color:#fff">e.</b> info@meridaleholding.com</div>
  <div class="footer-head" style="left:616px">Meridale Holding Partners</div>
  <div class="footer-addr">Lorem 62 Ipsum work dummy</div>
  <div class="footer-small" style="left:616px;top:2809px">Lorem Ipsum, Ma-300960</div>
  <svg class="abs" style="left:1094px;top:2746px" width="20" height="24" viewBox="0 0 20 24" aria-label="Back to top">
    <path d="M10 22 V3 M2 10 L10 2 L18 10" fill="none" stroke="#ef8a3c" stroke-width="2"/>
  </svg>
  <div class="footer-rule"></div>
  <div class="copyright">© 2020 <span>Meridale Holding Partners.</span> All Rights Reserved</div>
  <div class="social" style="left:964px"></div>
  <div class="social" style="left:1003px"></div>
  <div class="social" style="left:1041px"></div>
  <div class="social" style="left:1080px"></div>

</div>
</body>
</html>
```